Selvin: A Friday night in the Prophetic Flyer

We are holding 2 Friday night events, one on 10/25/19 and the other on 11/29/19.
The time frame is 6:30pm-9:00pm. These services will be a time of prayer/healing for the sick and will be prophetic as well. (There will be prophets prophesying over people)

The event is called: Selvin: A Friday night in the Prophetic
The flyer should also include the phrase/excerpt: "And they prophesied also".

Keywords/Phrases: Prophetic, Healing, Climbing in the Spirit, Higher level of Anointing...

Target Market(s)

those looking for healing, seeking a word from God

Colors

Designer to choose colors to be used in the design.

Requirements
Must have
• The event is called: Selvin: A Friday night in the Prophetic
• The flyer should also include the phrase/excerpt: "And they prophesied also".
• It must include the Tovik logo attached, either is fine, we have attached two different versions.
• It must have the dates, location, time
• Dates: October 25, 2019 and November 29, 2019
• Location: Hollard Community Center
• (Downtown Portland) 482 Wendle Street
• Portland, ME 04102
• Time: 6:30pm-9:00pm
• Contact Info: Tel. 207-555-3841
• email: contact@brimfield-hall.org
• web: www.tovik.org
Nice to have
• creativity in color scheme, the meaning of the word Selvin conveyed in a classy artistic way/design.
Should not have
• Crosses, pictures of churches

```html
<!DOCTYPE html>
<html lang="en">
<head>
<meta charset="utf-8">
<title>Selvin: A Friday Night in the Prophetic – Flyer</title>
<link rel="stylesheet" href="https://fonts.googleapis.com/css2?family=Anton&family=Cinzel:wght@400;600&family=Hind:wght@600;700&family=Source+Sans+3:wght@400;700&display=swap">
<style>
  :root{
    --backdrop:#383838;
    --navy:#0f3f68;
    --navy-deep:#0a2a48;
    --orange:#f7941d;
    --white:#ffffff;
    --ink:#14243a;
  }
  *{box-sizing:border-box;margin:0;padding:0}
  html,body{width:1200px;height:1200px;overflow:hidden;background:var(--backdrop)}
  .flyer{
    position:absolute;left:221px;top:75px;width:764px;height:1071px;
    background:var(--navy);overflow:hidden;color:var(--white);
    font-family:"Source Sans 3",sans-serif;
    box-shadow:0 4px 14px rgba(0,0,0,.45);
  }
  .hero-photo{
    position:absolute;left:0;top:0;width:764px;height:545px;
    background:
      radial-gradient(ellipse 40% 45% at 50% 2%, #f4f6fb 0%, #b9c3dc 25%, rgba(90,105,150,.6) 55%, transparent 80%),
      radial-gradient(ellipse 35% 55% at 50% 55%, #b98f7c 0%, #8a6052 40%, transparent 75%),
      linear-gradient(180deg,#34405f 0%,#1d2640 55%,#0b0f1c 100%);
  }
  .hero-curve{position:absolute;left:0;top:0}
  .brand{
    position:absolute;left:0;width:100%;top:586px;text-align:center;
    font-family:"Cinzel",serif;font-weight:400;font-size:44px;letter-spacing:2px;color:var(--white);
  }
  .title-band{
    position:absolute;left:0;top:662px;width:100%;height:55px;background:var(--orange);
    display:flex;align-items:center;justify-content:center;
  }
  .title-band h1{
    font-family:"Anton",sans-serif;font-weight:400;font-size:41px;line-height:1;
    color:var(--white);text-shadow:2px 2px 2px rgba(60,30,0,.55);letter-spacing:.3px;
  }
  .excerpt-tab{
    position:absolute;left:99px;top:717px;width:547px;height:40px;background:var(--white);
    border-radius:0 0 26px 26px;display:flex;align-items:center;justify-content:center;
    font-family:"Cinzel",serif;font-size:29px;color:var(--ink);letter-spacing:1px;
  }
  .dates{
    position:absolute;left:144px;top:776px;
    font-family:"Hind",sans-serif;font-weight:700;font-size:37px;line-height:1;white-space:nowrap;
  }
  .year{
    position:absolute;left:596px;top:812px;transform:rotate(-90deg);transform-origin:left top;
    font-family:"Hind",sans-serif;font-weight:700;font-size:20px;letter-spacing:1px;
  }
  .time-pill{
    position:absolute;left:192px;top:830px;width:368px;height:41px;background:var(--orange);
    border-radius:21px;display:flex;align-items:center;justify-content:center;
    font-family:"Cinzel",serif;font-weight:400;font-size:29px;color:var(--white);
  }
  .time-pill small{font-size:22px}
  .event-badge{
    position:absolute;top:861px;width:106px;height:106px;border-radius:50%;background:var(--orange);
    display:flex;align-items:center;justify-content:center;text-align:center;
    font-family:"Hind",sans-serif;font-weight:600;font-size:17px;line-height:1.2;
  }
  .event-badge.left{left:37px}
  .event-badge.right{left:622px}
  .venue{
    position:absolute;left:0;width:100%;top:880px;text-align:center;
    font-family:"Hind",sans-serif;font-weight:700;font-size:24px;
  }
  .address{position:absolute;left:257px;top:913px;font-size:17px;line-height:21px}
  .pin{position:absolute;left:226px;top:922px}
  .contact{
    position:absolute;left:0;width:100%;top:966px;text-align:center;font-size:17px;
    display:flex;justify-content:center;align-items:center;gap:4px;
  }
  .contact svg{vertical-align:middle}
  .description{
    position:absolute;left:0;width:100%;top:994px;text-align:center;font-size:16.5px;line-height:21px;
  }
  .web-tab{
    position:absolute;left:169px;top:1042px;width:422px;height:32px;background:var(--white);
    border-radius:16px 16px 0 0;color:var(--ink);font-size:16.5px;
    display:flex;align-items:center;justify-content:center;gap:8px;
  }
  .web-tab strong{font-weight:700}
</style>
</head>
<body>
<article class="flyer">
  <div class="hero-photo" role="img" aria-label="Photograph of open cupped hands raised in prayer beneath a beam of light through dark smoke"></div>
  <svg class="hero-curve" width="764" height="560" viewBox="0 0 764 560" aria-hidden="true">
    <path d="M0 477 Q382 564 764 475 L764 560 L0 560 Z" fill="var(--orange)"/>
    <path d="M0 510 Q382 556 764 499 L764 560 L0 560 Z" fill="var(--navy)"/>
  </svg>

  <div class="brand">TOVIK</div>

  <div class="title-band"><h1>SELVIN : A FRIDAY NIGHT IN THE PROPHETIC</h1></div>
  <div class="excerpt-tab">"AND THEY PROPHESIED ALSO"</div>

  <div class="dates">October 25 | November 29</div>
  <div class="year">2019</div>

  <div class="time-pill">T<small>IME</small>&nbsp;-&nbsp;6:30<small>PM</small>-9:00<small>PM</small></div>

  <div class="event-badge left">2 Friday<br>Night<br>Events</div>
  <div class="event-badge right">2 Friday<br>Night<br>Events</div>

  <div class="venue">Hollard Community Center</div>
  <svg class="pin" width="16" height="22" viewBox="0 0 16 22" aria-hidden="true">
    <path d="M8 0C3.6 0 0 3.5 0 7.9 0 13.5 8 22 8 22s8-8.5 8-14.1C16 3.5 12.4 0 8 0z" fill="var(--orange)"/>
    <circle cx="8" cy="8" r="3" fill="var(--navy)"/>
  </svg>
  <div class="address">(Downtown Portland) 482 Wendle Street<br>Portland, ME 04102</div>

  <div class="contact">
    <span>Contact Info :</span>
    <svg width="22" height="22" viewBox="0 0 22 22" aria-hidden="true">
      <circle cx="11" cy="11" r="10" fill="none" stroke="var(--white)" stroke-width="1.5"/>
      <path d="M7.5 6.5l2 .2.8 2.4-1.2 1c.6 1.3 1.6 2.3 2.9 2.9l1-1.2 2.4.8.2 2c-.4.6-1.2.9-2 .8-3.6-.5-6.6-3.5-7.1-7.1-.1-.8.3-1.5.9-1.8z" fill="var(--white)"/>
    </svg>
    <span>207-555-3841 |</span>
    <svg width="22" height="16" viewBox="0 0 22 16" aria-hidden="true">
      <rect x="1" y="2" width="20" height="13" fill="none" stroke="var(--white)" stroke-width="1.6"/>
      <path d="M1 2l10 8 10-8M1 15l7-6M21 15l-7-6" fill="none" stroke="var(--white)" stroke-width="1.6"/>
    </svg>
    <span>contact@brimfield-hall.org</span>
  </div>

  <p class="description">These services will be a time of prayer/healing for the sick and will be prophetic as well.<br>(There will be prophets prophesying over people)</p>

  <div class="web-tab">
    <span>Visit our website for more details</span>
    <svg width="18" height="18" viewBox="0 0 18 18" aria-hidden="true">
      <circle cx="9" cy="9" r="8" fill="none" stroke="var(--orange)" stroke-width="1.5"/>
      <ellipse cx="9" cy="9" rx="3.5" ry="8" fill="none" stroke="var(--orange)" stroke-width="1.2"/>
      <path d="M1 9h16M2.5 5h13M2.5 13h13" stroke="var(--orange)" stroke-width="1.2"/>
    </svg>
    <strong>www.tovik.org</strong>
  </div>
</article>
</body>
</html>
```